Poster for Pool Party Event

We run a music booking and management agency Brindlewave (www.brindlewave.com.au). We're throwing a pool party to showcase the best of our agency at the luxurious Moss Deck in Sydney.
It's a day/night party. We need an amazing poster. Here is the venue's FB page, check some of their previous posters to get an idea of what they do https://www.facebook.com/lagoonrooftop - ours has to be a little more sophisticated/edgy/indie. Less clichéd that your standard stock photo of a babe lying by a pool. The vibe is a really cool brand throwing a huge pool party, a party you'd die to get tickets to.
Yes we definitely want a babe or a few babes in it, but we don't want that to necessarily be too overbearing. Also open to artistic interpretations - something original and outside of the box. Minimal if it works - bright and fun, but professional and edgy at the same time. Preferrably include water or something eluding to it being actually at a pool.
Basic info to include:
Title in some kind of awesome font at the top: Brindlewave Pool Party
Date: Sat 24 March
Leave enough space for the event lineup and info at the bottom, usually around a 3rd of the poster needs to be an area that's relatively clear for the lineup and info.
Crucial that the event accurately represents the Brindlewave brand. Boutique indie music company, innovative and awesome parties, respected party DJs and great indie bands.
Some photos from recent similar parties there to give you an idea of the vibe:
http://quillmarrow.com/galleries.cfm?id=651
http://quillmarrow.com/galleries.cfm?id=650
http://quillmarrow.com/galleries.cfm?id=649
Target Market(s)
18-25 year olds. Music lovers. Party lovers. Music industry. Babes.
Industry/Entity Type
Boutique
Look and feel

```html
<!DOCTYPE html>
<html lang="en">
<head>
<meta charset="utf-8">
<title>Brindlewave Pool Party</title>
<link rel="stylesheet" href="https://fonts.googleapis.com/css2?family=Monoton&family=Oswald:wght@700&family=Silkscreen:wght@400;700&display=swap">
<style>
  :root {
    --night: #0b0d12;
    --pool-deep: #0f4f96;
    --pool-mid: #1e7fc8;
    --pool-light: #3fa6de;
    --vinyl-dark: #2a1206;
    --vinyl-glow: #c9621f;
    --title-yellow: #fff35a;
    --shadow-blue: #1d9fe6;
    --shadow-green: #23b14d;
    --shadow-red: #e8253a;
    --shadow-magenta: #e0209a;
    --white: #ffffff;
    --ink: #15181d;
    --panel-fill: rgba(150, 215, 245, 0.28);
    --panel-edge: rgba(120, 200, 120, 0.55);
  }
  * { margin: 0; padding: 0; box-sizing: border-box; }
  html, body { width: 800px; height: 1200px; overflow: hidden; background: var(--night); }
  .poster {
    position: relative;
    width: 800px;
    height: 1200px;
    overflow: hidden;
    font-family: "Silkscreen", monospace;
  }
  .pool-photo {
    position: absolute; inset: 0;
    background:
      radial-gradient(ellipse 300px 420px at 330px 720px, rgba(200,230,245,0.35), transparent 70%),
      linear-gradient(180deg, var(--night) 0%, #12243f 17%, var(--pool-deep) 32%, var(--pool-mid) 60%, var(--pool-light) 100%);
  }
  .turntable-photo {
    position: absolute; left: 427px; top: 0; width: 373px; height: 287px;
    background:
      radial-gradient(ellipse 220px 160px at 210px 120px, var(--vinyl-glow), var(--vinyl-dark) 65%, transparent 100%);
  }
  .brand {
    position: absolute; left: 24px; top: 44px;
    display: flex; align-items: center; gap: 22px;
  }
  .brand-mark {
    width: 93px; height: 93px; border-radius: 10px;
    background: var(--white);
  }
  .brand-name {
    font-family: "Oswald", sans-serif;
    font-size: 84px; font-weight: 700; line-height: 1;
    color: var(--white); text-transform: uppercase; letter-spacing: 2px;
  }
  .title {
    position: absolute; font-family: "Monoton", cursive; color: var(--title-yellow); line-height: 1;
    white-space: nowrap;
  }
  .title-pool {
    left: 26px; top: 170px; font-size: 164px;
    text-shadow: -10px -8px 0 var(--shadow-blue), -5px -4px 0 var(--shadow-green);
  }
  .title-party {
    left: 352px; top: 358px; font-size: 96px;
    text-shadow: -9px -7px 0 var(--shadow-magenta), -4px -3px 0 var(--shadow-red);
  }
  .date {
    position: absolute; left: 52px; top: 396px;
    font-size: 24px; font-weight: 700; color: var(--white); white-space: nowrap;
    text-shadow: -3px -3px 0 var(--shadow-magenta);
  }
  .info-panel {
    position: absolute; left: 22px; top: 640px; width: 757px; height: 520px;
    border-radius: 42px;
    background: var(--panel-fill);
    border: 4px solid var(--panel-edge);
  }
  .info-heading {
    position: absolute; left: 44px; top: 46px;
    font-size: 27px; font-weight: 700; color: var(--ink); white-space: nowrap;
  }
</style>
</head>
<body>
  <main class="poster">
    <div class="pool-photo" role="img" aria-label="Underwater pool photo with blue tiles and a swimmer diving through bubbles"></div>
    <div class="turntable-photo" role="img" aria-label="Close-up photo of a record spinning on a turntable"></div>

    <header class="brand">
      <div class="brand-mark"></div>
      <span class="brand-name">Brindlewave</span>
    </header>

    <h1>
      <span class="title title-pool">POOL</span>
      <span class="title title-party">PARTY</span>
    </h1>
    <p class="date">Sat 24 March</p>

    <section class="info-panel">
      <h2 class="info-heading">EVENT LINEUP &amp; INFO</h2>
    </section>
  </main>
</body>
</html>
```